Sample site of what the customer is looking for:
www.tressivocars.example - he doesn't like the girl in the background

- Looking for something easy to navigate, simple, yet different like Tressivo Cars

- For the background image, he's looking for a dusky night scene with a car or a road or something like that

- Accent color - match the logo which is attached unless a different color works better with the design

- Phone number: 555-014-7263

- The buttons for the menu will be: Home, Inventory, About Us & Contact Us

- No content on the homepage

```html
<!DOCTYPE html>
<html lang="en">
<head>
<meta charset="utf-8">
<title>Corvane Auto Collective</title>
<link rel="stylesheet" href="https://fonts.googleapis.com/css2?family=Mulish:wght@300;400;500;600&display=swap">
<style>
  :root {
    --header-bg: #ffffff;
    --nav-text: #4a4a4a;
    --brand-navy: #123a5c;
    --brand-maroon: #7a3a3c;
    --hero-deep: #0c0f1c;
    --hero-mid: #2a3048;
    --hero-light: #5c6482;
    --text-light: #f4f4f6;
    --text-muted: #a8abb8;
    --rule: rgba(255,255,255,0.22);
    --button-bg: rgba(60,60,62,0.85);
    --button-border: rgba(255,255,255,0.35);
    --dot-idle: #b9b9bd;
    --dot-active: #6e3a3c;
    --social-1: #3f5f94;
    --social-2: #3fa3b0;
    --social-3: #c9482e;
  }
  * { box-sizing: border-box; margin: 0; padding: 0; }
  html, body { width: 1200px; height: 738px; overflow: hidden; }
  body { font-family: "Mulish", sans-serif; background: var(--hero-deep); position: relative; }

  .site-header {
    position: absolute; left: 0; top: 0; width: 1200px; height: 107px;
    background: var(--header-bg);
  }
  .brand {
    position: absolute; left: 74px; top: 24px;
    display: flex; align-items: center; gap: 10px;
    color: var(--brand-navy); font-weight: 600; font-size: 19px; line-height: 1.15;
  }
  .brand-mark { width: 14px; height: 14px; border-radius: 50%; background: var(--brand-navy); flex: none; }
  .main-nav { position: absolute; left: 267px; top: 44px; display: flex; gap: 0; }
  .main-nav a {
    color: var(--nav-text); text-decoration: none; font-size: 15px; font-weight: 500;
    position: absolute; white-space: nowrap;
  }
  .phone {
    position: absolute; right: 74px; top: 43px;
    color: var(--brand-navy); font-size: 17.5px; font-weight: 600;
  }

  .hero {
    position: absolute; left: 0; top: 107px; width: 1200px; height: 631px;
  }
  .hero-backdrop {
    position: absolute; inset: 0;
    background:
      radial-gradient(ellipse 320px 220px at 235px 290px, rgba(200,205,225,0.45), transparent 70%),
      radial-gradient(ellipse 240px 120px at 900px 180px, rgba(150,30,40,0.35), transparent 70%),
      linear-gradient(180deg, var(--hero-light) 0%, var(--hero-mid) 35%, #1a1e30 65%, var(--hero-deep) 100%);
  }
  .hero-title {
    position: absolute; left: 0; width: 1200px; top: 238px; text-align: center;
    color: var(--text-light); font-size: 33px; font-weight: 500; letter-spacing: 0.2px;
    text-shadow: 0 1px 3px rgba(0,0,0,0.5);
  }
  .hero-button {
    position: absolute; left: 517px; top: 307px; width: 166px; height: 45px;
    background: var(--button-bg); border: 1px solid var(--button-border); border-radius: 2px;
    color: var(--text-light); font-size: 21px; font-weight: 600;
    display: flex; align-items: center; justify-content: center; text-decoration: none;
  }
  .slider-dots { position: absolute; left: 567px; top: 436px; display: flex; gap: 5.5px; }
  .slider-dots span { width: 12px; height: 12px; border-radius: 50%; background: var(--dot-idle); }
  .slider-dots .is-active { background: var(--dot-active); }

  .site-footer { position: absolute; left: 74px; top: 630px; width: 1052px; height: 108px; border-top: 1px solid var(--rule); }
  .footer-nav { position: absolute; left: 0; top: 19px; }
  .footer-nav a { position: absolute; white-space: nowrap; color: var(--text-muted); text-decoration: none; font-size: 12.5px; font-weight: 300; }
  .copyright { position: absolute; left: 0; top: 60px; color: var(--text-muted); font-size: 11px; font-weight: 300; line-height: 16px; }
  .copyright strong { color: var(--text-light); font-weight: 400; }
  .social { position: absolute; right: 0; top: 44px; display: flex; align-items: center; gap: 4px; }
  .social-label { color: var(--text-muted); font-size: 14px; font-weight: 300; margin-right: 12px; }
  .social-link { width: 30px; height: 30px; border-radius: 50%; display: block; }
  .social-link.one { background: var(--social-1); }
  .social-link.two { background: var(--social-2); }
  .social-link.three { background: var(--social-3); }
</style>
</head>
<body>
  <header class="site-header">
    <div class="brand"><span class="brand-mark"></span><span>Corvane<br>Auto Collective</span></div>
    <nav class="main-nav">
      <a href="#" style="left:0">Home</a>
      <a href="#" style="left:75px">Inventory</a>
      <a href="#" style="left:174px">About Us</a>
      <a href="#" style="left:272px">Contact Us</a>
    </nav>
    <div class="phone">Phone Number: 555-014-7263</div>
  </header>

  <main class="hero">
    <div class="hero-backdrop" role="img" aria-label="Dusky night scene of a dark luxury coupe parked by a seaside railing with glowing red tail lights"></div>
    <h1 class="hero-title">Corvane Auto Collective, Arizona's Luxury Vehicle Providers.</h1>
    <a class="hero-button" href="#">Contact Us</a>
    <div class="slider-dots"><span class="is-active"></span><span></span><span></span><span></span></div>
  </main>

  <footer class="site-footer">
    <nav class="footer-nav">
      <a href="#" style="left:0">Home</a>
      <a href="#" style="left:52px">Inventory</a>
      <a href="#" style="left:130px">About Us</a>
      <a href="#" style="left:196px">Contact Us</a>
    </nav>
    <p class="copyright">Copyright © 2014. <strong>Corvane Auto Collective.</strong><br>All Right Reserved</p>
    <div class="social">
      <span class="social-label">Connect Us:</span>
      <a class="social-link one" href="#" aria-label="Social profile"></a>
      <a class="social-link two" href="#" aria-label="Social profile"></a>
      <a class="social-link three" href="#" aria-label="Video channel"></a>
    </div>
  </footer>
</body>
</html>
```